Creative, Striking, Responsive Tutoring Flyer

I need a designer superstar to create an attractive, modern and eye-catching flyer for me. I'm a teacher and I need the flyer to sell French & German private lessons.

Attached is an example that I like a lot. Please create a similar design.

```html
<!DOCTYPE html>
<html lang="en">
<head>
<meta charset="utf-8">
<title>French &amp; German Private Lessons Flyer</title>
<link rel="stylesheet" href="https://fonts.googleapis.com/css2?family=Alfa+Slab+One&family=Roboto:wght@500&family=Roboto+Condensed:wght@500&family=Roboto+Slab:wght@400;500;600&display=swap">
<style>
  :root {
    --stage-top: #c4c4c4;
    --stage-bottom: #8e8e8e;
    --board-dark: #2a2d31;
    --board-mid: #42464c;
    --chalk: #f2f2f2;
    --highlight: #f7f201;
    --ink: #1d1d1d;
    --supplies-a: #4b5a66;
    --supplies-b: #6f8a3a;
    --supplies-c: #d9932b;
    --skyline-light: #e6e6e6;
    --skyline-mid: #a4a4a4;
  }
  * { margin: 0; padding: 0; box-sizing: border-box; }
  html, body { width: 1200px; height: 927px; overflow: hidden; }
  body {
    position: relative;
    background: linear-gradient(180deg, var(--stage-top), var(--stage-bottom));
    font-family: "Roboto Slab", serif;
    color: var(--chalk);
  }
  .flyer {
    position: absolute;
    top: 94px;
    width: 564px;
    height: 729px;
    overflow: hidden;
    background: radial-gradient(ellipse at 55% 20%, var(--board-mid), var(--board-dark) 75%);
    text-align: center;
  }
  .flyer--front { left: 24px; }
  .flyer--back { left: 612px; }

  .headline {
    position: absolute;
    left: 0; right: 0;
    font-family: "Alfa Slab One", serif;
    line-height: 1;
    white-space: nowrap;
  }
  .headline--chalk { color: var(--chalk); }
  .headline--yellow { color: var(--highlight); }

  .front-line-1 { top: 30px; font-size: 70px; letter-spacing: 3px; padding-left: 8px; }
  .front-line-2 { top: 104px; font-size: 74px; letter-spacing: 1px; }
  .front-line-3 { top: 180px; font-size: 43px; letter-spacing: 1px; padding-left: 8px; }

  .name-ribbon { position: absolute; left: 57px; top: 256px; width: 436px; height: 86px; }
  .name-ribbon__text {
    position: absolute; left: 66px; top: 14px; width: 302px;
    font-family: "Roboto Condensed", sans-serif; font-weight: 500;
    font-size: 36px; line-height: 40px; color: var(--ink); white-space: nowrap;
  }

  .role { position: absolute; left: 0; right: 0; top: 336px; font-size: 21px; line-height: 26px; font-weight: 600; }
  .phone { position: absolute; left: 0; right: 0; top: 366px; font-family: "Roboto", sans-serif; font-weight: 500; font-size: 44px; line-height: 52px; }
  .email { position: absolute; left: 0; right: 0; top: 414px; font-size: 29px; line-height: 36px; }
  .social {
    position: absolute; left: 0; right: 0; top: 460px;
    font-size: 18px; line-height: 24px; display: flex; justify-content: center; align-items: center; gap: 10px;
  }
  .social__dot { width: 16px; height: 16px; border-radius: 50%; background: var(--chalk); }

  .supplies-art {
    position: absolute; left: 0; bottom: 0; width: 564px; height: 230px;
    background:
      radial-gradient(ellipse at 15% 85%, var(--supplies-b), transparent 35%),
      radial-gradient(ellipse at 85% 80%, var(--supplies-c), transparent 40%),
      linear-gradient(180deg, transparent, var(--supplies-a) 55%);
  }

  .back-line-1 { top: 56px; font-size: 39px; letter-spacing: 1px; }
  .back-line-2 { top: 99px; font-size: 33px; letter-spacing: 0.5px; }

  .copy {
    position: absolute; left: 48px; width: 468px;
    font-size: 11px; line-height: 15px;
  }
  .copy--1 { top: 154px; }
  .copy--2 { top: 274px; }
  .copy--3 { top: 352px; }
  .copy--4 { top: 419px; }

  .skyline-art {
    position: absolute; left: 0; bottom: 0; width: 564px; height: 235px;
    background: linear-gradient(180deg, rgba(164,164,164,0) 0%, var(--skyline-mid) 65%, var(--skyline-light) 100%);
  }
</style>
</head>
<body>
  <section class="flyer flyer--front">
    <div class="headline headline--chalk front-line-1">FRENCH &amp;</div>
    <div class="headline headline--chalk front-line-2">GERMAN</div>
    <div class="headline headline--yellow front-line-3">PRIVATE LESSONS</div>

    <div class="name-ribbon">
      <svg width="436" height="86" viewBox="0 0 436 86" aria-hidden="true">
        <polygon points="0,17 60,17 54,83 0,83 30,50" fill="var(--highlight)"/>
        <polygon points="376,17 436,17 406,50 436,83 370,83" fill="var(--highlight)"/>
        <rect x="66" y="0" width="302" height="66" fill="var(--highlight)"/>
      </svg>
      <div class="name-ribbon__text">CLAIRE HARTMANN</div>
    </div>

    <div class="role">OUR PERSONAL TRAINER</div>
    <div class="phone">800-555-0192</div>
    <div class="email">bonjour@sprachklasse.com</div>
    <div class="social"><span class="social__dot"></span><span>@sprachklasse.lessons</span></div>

    <div class="supplies-art" role="img" aria-label="School supplies spread across the bottom: apple, notebook, scissors, markers, coloured pencils, paper clips, push pins and a calculator"></div>
  </section>

  <section class="flyer flyer--back">
    <div class="headline headline--chalk back-line-1">FRENCH &amp; GERMAN</div>
    <div class="headline headline--yellow back-line-2">PRIVATE LESSONS</div>

    <p class="copy copy--1">Lorem ipsum dolor sit amet, consectetur adipiscing elit, sed do eiusmod tempor incididunt ut labore et dolore magna aliqua. Ut enim ad minim veniam, quis nostrud exercitation ullamco laboris nisi ut aliquip ex ea commodo consequat. Duis aute irure dolor in reprehenderit in voluptate velit esse cillum dolore eu fugiat nulla pariatur. Excepteur sint occaecat cupidatat non proident, sunt in culpa qui officia deserunt mollit anim id est laborum.</p>
    <p class="copy copy--2">Lorem ipsum dolor sit amet, consectetur adipiscing elit, sed do eiusmod tempor incididunt ut labore et dolore magna aliqua. Ut enim ad minim veniam, quis nostrud exercitation ullamco laboris nisi ut aliquip ex ea commodo consequat.</p>
    <p class="copy copy--3">Duis aute irure dolor in reprehenderit in voluptate velit esse cillum dolore eu fugiat nulla pariatur. Excepteur sint occaecat cupidatat non proident, sunt in culpa qui officia deserunt mollit anim id est laborum.</p>
    <p class="copy copy--4">Sed ut perspiciatis unde omnis iste natus error sit voluptatem accusantium doloremque laudantium, totam rem aperiam, eaque ipsa quae ab illo inventore veritatis et quasi architecto beatae vitae dicta sunt explicabo.</p>

    <div class="skyline-art" role="img" aria-label="Pale skyline of Paris and Berlin landmarks with trees, clouds and birds"></div>
  </section>
</body>
</html>
```